Holvern Incorporated

Holvern is a business that provides consulting, and manages and supplies trades persons in the construction and heavy industries sector. We build, do maintenance, install machinery, and can manage projects or jobs. Would like or prefer more clean, classic designs. Blacks/greys, but open to almost anything.

Target Market(s)

Industrial/Construction/Manufacturing

Industry/Entity Type

Construction Company

Contact Information for Business Card

Clean, business name on the front, possibly have the details on the back, but open to any ideas.

Logo Text

We currently do not have a slogan, open to ideas

Font styles to use
Serif
Sans Serif

Colors

Designer to choose colors to be used in the design.

Requirements
Should not have
• the oval is not my logo, was just an idea. please don't send 20 designs with the oval

```html
<!DOCTYPE html>
<html lang="en">
<head>
<meta charset="utf-8">
<title>Holvern Incorporated – Business Card</title>
<link href="https://fonts.googleapis.com/css2?family=Bitter:wght@600&family=Oxygen:wght@400&display=swap" rel="stylesheet">
<style>
  :root {
    --navy: #1a202c;
    --sky: #6aaee0;
    --orange: #e07a2a;
    --paper: #ffffff;
    --ink: #1c1f26;
    --backdrop: #3b3a38;
  }
  * { box-sizing: border-box; margin: 0; padding: 0; }
  html, body {
    width: 1200px; height: 1200px; overflow: hidden;
    background: var(--backdrop);
  }
  .sheet {
    width: 1200px; height: 1200px;
    display: flex; flex-direction: column;
    align-items: center; justify-content: center; gap: 60px;
  }
  .card {
    position: relative;
    width: 840px; height: 480px;
    overflow: hidden;
    box-shadow: 0 10px 30px rgba(0,0,0,.35);
  }

  /* Front */
  .card--front { background: var(--navy); }
  .front-name {
    position: absolute; left: 0; right: 0; top: 150px;
    text-align: center;
    font-family: "Bitter", Georgia, serif; font-weight: 600;
    font-size: 104px; letter-spacing: 2px; line-height: 1.1;
    color: var(--paper);
  }
  .front-rule {
    position: absolute; left: 0; right: 0; bottom: 48px;
    height: 10px; background: var(--sky);
  }
  .front-rule::before {
    content: ""; position: absolute; left: 0; top: 0;
    width: 120px; height: 100%; background: var(--orange);
  }

  /* Back */
  .card--back { background: var(--paper); }
  .back-header {
    position: absolute; left: 0; right: 0; top: 0;
    height: 150px; background: var(--navy);
    border-bottom: 10px solid var(--sky);
  }
  .back-name {
    position: absolute; left: 60px; top: 42px;
    font-family: "Bitter", Georgia, serif; font-weight: 600;
    font-size: 48px; letter-spacing: 1px; line-height: 1.2;
    color: var(--paper);
  }
  .person { position: absolute; left: 70px; top: 292px; color: var(--ink);
    font-family: "Oxygen", Arial, sans-serif; }
  .person-name { font-size: 36px; letter-spacing: 1px; line-height: 1.1; }
  .person-title { font-size: 22px; letter-spacing: .5px; margin-top: 4px; }

  .contact {
    position: absolute; left: 440px; top: 238px;
    border-left: 2px solid var(--orange);
    padding-left: 34px; height: 150px;
    font-family: "Oxygen", Arial, sans-serif; font-size: 19px;
    letter-spacing: .6px; color: var(--ink);
  }
  .contact-line { position: relative; height: 40px; line-height: 24px; }
  .contact-line--address { height: auto; }
  .contact-icon {
    position: absolute; left: -78px; top: 2px; width: 24px; height: 24px;
    stroke: var(--orange); fill: none; stroke-width: 1.6;
    stroke-linejoin: round; stroke-linecap: round;
  }
</style>
</head>
<body>
<main class="sheet">

  <section class="card card--front" aria-label="Card front">
    <div class="front-name">Holvern</div>
    <div class="front-rule" aria-hidden="true"></div>
  </section>

  <section class="card card--back" aria-label="Card back">
    <div class="back-header" aria-hidden="true"></div>
    <div class="back-name">Holvern</div>

    <div class="person">
      <div class="person-name">Daniel Rowe</div>
      <div class="person-title">Operations Manager</div>
    </div>

    <div class="contact">
      <div class="contact-line">
        <svg class="contact-icon" viewBox="0 0 24 24" aria-hidden="true"><path d="M2 11 22 3 15 21 11 13Z M11 13 22 3"/></svg>
        drowe@holvern.com
      </div>
      <div class="contact-line">
        <svg class="contact-icon" viewBox="0 0 24 24" aria-hidden="true"><path d="M5 3h4l2 5-3 2a11 11 0 0 0 6 6l2-3 5 2v4a2 2 0 0 1-2 2A17 17 0 0 1 3 5a2 2 0 0 1 2-2Z"/></svg>
        555-204-318-6
      </div>
      <div class="contact-line contact-line--address">
        <svg class="contact-icon" viewBox="0 0 24 24" aria-hidden="true"><path d="M3 11 12 4l9 7M5 10v10h14V10M10 20v-5h4v5"/></svg>
        4182 Larkfield Ave.<br>Brenton, NJ 07412
      </div>
    </div>
  </section>

</main>
</body>
</html>
```